Brivora Collective Business Card Design

We need a business card design for Brivora Collective. We are a healthcare recruiting, wellness and education company. We partner with medical facilities to find quality candidates. We also offer free wellness courses.
The final design should communicate an emphasis on recruiting and wellness
The main purpose of the business card is to utilized it for networking events, give to hospitals, executives, VCs surgery centers and clinics. I want it to be sleek, clean, use of our brand colors and professional.

```html
<!DOCTYPE html>
<html lang="en">
<head>
<meta charset="utf-8">
<title>Brivora Collective Business Card</title>
<link rel="stylesheet" href="https://fonts.googleapis.com/css2?family=Arimo:wght@400;700&display=swap">
<style>
  :root {
    --brand-green: #005a50;
    --brand-green-light: #0f7a6d;
    --brand-green-soft: #2a8a7d;
    --ink: #1a1a1a;
    --muted: #6b6b6b;
    --rule: #b9b9b9;
    --paper: #ffffff;
    --stage: #1f1f1f;
  }
  * { box-sizing: border-box; margin: 0; padding: 0; }
  html, body {
    width: 1200px; height: 1108px; overflow: hidden;
    background: var(--stage);
    font-family: "Arimo", Arial, sans-serif;
  }
  .canvas {
    position: relative; width: 1200px; height: 1108px;
    display: flex; justify-content: center; align-items: center; gap: 60px;
  }
  .card {
    width: 400px; height: 700px; border-radius: 26px; overflow: hidden;
    position: relative;
  }
  .card-front {
    background: var(--paper);
    display: flex; flex-direction: column; align-items: center;
    padding: 110px 40px 0;
    text-align: center;
  }
  .brand {
    display: flex; align-items: center; gap: 12px;
    color: var(--brand-green);
    font-weight: 700; font-size: 34px; line-height: 1.1;
  }
  .brand-mark {
    width: 22px; height: 22px; background: var(--brand-green); border-radius: 4px;
    flex-shrink: 0;
  }
  .person { margin-top: 90px; }
  .person-name {
    color: var(--brand-green); font-weight: 700; font-size: 30px; letter-spacing: 0.5px;
  }
  .person-title { color: var(--muted); font-size: 20px; margin-top: 2px; }
  .icon-row {
    display: flex; align-items: center; gap: 12px; margin-top: 22px; width: 100%;
  }
  .icon-row .rule { flex: 1; height: 1px; background: var(--rule); }
  .icon {
    width: 26px; height: 26px; border-radius: 6px; background: var(--brand-green);
    display: flex; align-items: center; justify-content: center;
  }
  .contact {
    margin-top: 16px; color: var(--ink); font-size: 19px; line-height: 1.45;
  }
  .divider { width: 100%; height: 1px; background: var(--rule); margin: 22px 0 26px; }
  .address { color: var(--ink); font-size: 19px; line-height: 1.45; }
  .card-back {
    background: var(--brand-green);
  }
  .back-pattern {
    position: absolute; inset: 0;
    background: linear-gradient(135deg, var(--brand-green) 0%, var(--brand-green-light) 60%, var(--brand-green-soft) 100%);
  }
  .back-mark {
    position: absolute; right: 96px; bottom: 150px;
    width: 36px; height: 36px; background: var(--paper); border-radius: 6px;
  }
</style>
</head>
<body>
<main class="canvas">
  <section class="card card-front" aria-label="Card front">
    <div class="brand">
      <span class="brand-mark"></span>
      <span class="brand-name">Brivora Collective</span>
    </div>
    <div class="person">
      <p class="person-name">Marcus Hale</p>
      <p class="person-title">President</p>
    </div>
    <div class="icon-row">
      <span class="rule"></span>
      <span class="icon" aria-label="Phone">
        <svg width="16" height="16" viewBox="0 0 24 24"><path fill="#fff" d="M6.6 10.8a15.1 15.1 0 0 0 6.6 6.6l2.2-2.2c.3-.3.7-.4 1-.2 1.1.4 2.3.6 3.6.6.6 0 1 .4 1 1V20c0 .6-.4 1-1 1C10.6 21 3 13.4 3 4c0-.6.4-1 1-1h3.5c.6 0 1 .4 1 1 0 1.3.2 2.5.6 3.6.1.3 0 .7-.2 1z"/></svg>
      </span>
      <span class="icon" aria-label="Email">
        <svg width="16" height="16" viewBox="0 0 24 24"><rect x="3" y="6" width="18" height="12" rx="1.5" fill="#fff"/><path d="M3.5 6.5 12 13l8.5-6.5" fill="none" stroke="#005a50" stroke-width="1.6"/></svg>
      </span>
      <span class="icon" aria-label="Website">
        <svg width="16" height="16" viewBox="0 0 24 24"><circle cx="12" cy="12" r="8.5" fill="none" stroke="#fff" stroke-width="2"/><path d="M3.5 12h17M12 3.5c3 3 3 14 0 17M12 3.5c-3 3-3 14 0 17" fill="none" stroke="#fff" stroke-width="1.5"/></svg>
      </span>
      <span class="rule"></span>
    </div>
    <div class="contact">
      <p>(555) 0147-2290</p>
      <p>name@brivoracollective.com</p>
      <p>www.brivoracollective.com</p>
    </div>
    <div class="divider"></div>
    <div class="address">
      <p>2716 Linden Crest Road</p>
      <p>Harbor Vale, NY 10990</p>
    </div>
  </section>

  <section class="card card-back" aria-label="Card back">
    <div class="back-pattern" role="img" aria-label="Repeating brand pattern in tonal green"></div>
    <span class="back-mark"></span>
  </section>
</main>
</body>
</html>
```